Etiketten für Honiggläser
Zielgruppe
Ich bin ein Imker und möchte meinen Honig verkaufen.
Aufgabenstellung
Ich möchte exklusive und edle Honigetiketten die auffallen. Ich habe weder ein Logo noch hat meine Imkerei einen Namen. ( Vorschläge sind aber auch willkommen ).
Auf die Vorderseite des Honigetiketts soll zu lesen sein:
- Deutscher Honig
- Art des Honigs: Blütenhonig / Waldhonig ...
- 500g
Auf der Rückseite des Honigetiketts soll zu finden sein:
- Namen und Adresse des Imkers
- freies Feld für das Mindesthaltbarkeitsdatum
Ergänzende Informationen:
- Name: Tobias Wend
- Adresse: Lindauer Gasse 47, 85399 Eggmoos ( Bayern )
Bitte in einem Format liefern, dass ich ohne Aufwände an eine Druckerei übergeben kann. Außerdem muss ich die Dateien bearbeiten können in Photoshop o.ä. um zB die Art des Honigs und die Füllmenge anpassen zu können.
Wichtig:
Die Abmessungen des Labels sollen 15,5cm - 17cm breit und 6cm hoch sein.

```html
<!DOCTYPE html>
<html lang="de">
<head>
<meta charset="utf-8">
<title>Blütenhonig – Etikett</title>
<link href="https://fonts.googleapis.com/css2?family=Courier+Prime&family=Pinyon+Script&family=Special+Elite&display=swap" rel="stylesheet">
<style>
  :root {
    --ink-rust: #863b2e;
    --paper: #ffffff;
    --art-dark: #3a3a3a;
    --art-mid: #9a9a9a;
  }
  html, body {
    margin: 0;
    padding: 0;
    overflow: hidden;
    background: var(--paper);
  }
  .label {
    position: relative;
    width: 1200px;
    height: 441px;
    background: var(--paper);
    color: var(--ink-rust);
    font-family: "Courier Prime", "Courier New", monospace;
    overflow: hidden;
  }
  .care-notes {
    position: absolute;
    left: 12px;
    bottom: 6px;
    writing-mode: vertical-rl;
    transform: rotate(180deg);
    font-size: 12px;
    line-height: 20px;
    white-space: nowrap;
  }
  .honey-type {
    position: absolute;
    left: 0;
    width: 1202px;
    top: 28px;
    text-align: center;
    font-family: "Pinyon Script", cursive;
    font-size: 34px;
    line-height: 1;
  }
  .hive-illustration {
    position: absolute;
    left: 398px;
    top: 94px;
    width: 404px;
    height: 237px;
  }
  .product-title {
    position: absolute;
    left: 0;
    width: 1208px;
    top: 358px;
    text-align: center;
    font-family: "Special Elite", "Courier New", monospace;
    font-size: 23px;
    letter-spacing: 0.3em;
    line-height: 1;
  }
  .beekeeper {
    position: absolute;
    left: 1008px;
    width: 160px;
    top: 38px;
    text-align: center;
    font-style: normal;
    font-size: 13px;
    line-height: 20.5px;
  }
  .pack-info {
    position: absolute;
    right: 30px;
    top: 326px;
    text-align: right;
    font-size: 12.5px;
  }
  .pack-info p { margin: 0; line-height: 18px; }
  .pack-info .best-before { margin-top: 11px; }
</style>
</head>
<body>
<div class="label">
  <div class="care-notes">
    Honig kann fest werden. Kristallisierten Honig im Wasserbad<br>
    (40C) wieder verflüssigen. Honig ist für Säuglinge unter 12<br>
    Monaten nicht geeignet.
  </div>

  <div class="honey-type">Blütenhonig</div>

  <svg class="hive-illustration" viewBox="0 0 404 237" role="img" aria-label="Holzstich-Illustration eines Bienenkorbs auf einer Bank, umgeben von Blumen, Sträuchern und Bienen">
    <defs>
      <radialGradient id="hive-tone" cx="52%" cy="55%" r="55%">
        <stop offset="0%" stop-color="var(--art-dark)" stop-opacity="0.55"/>
        <stop offset="60%" stop-color="var(--art-mid)" stop-opacity="0.35"/>
        <stop offset="100%" stop-color="var(--art-mid)" stop-opacity="0"/>
      </radialGradient>
    </defs>
    <ellipse cx="202" cy="130" rx="202" ry="118" fill="url(#hive-tone)"/>
  </svg>

  <div class="product-title">Deutscher Bienenhonig</div>

  <address class="beekeeper">
    Tobias Wend<br>
    Lindauer Gasse 47<br>
    85399 Eggmoos<br>
    (Bayern)
  </address>

  <div class="pack-info">
    <p class="net-weight">500 g</p>
    <p class="storage">Kühl, trocken und dunkel lagern.</p>
    <p class="best-before">Mindestens haltbar bis:</p>
  </div>
</div>
</body>
</html>
```